Product Insert / Thank You

I'm looking for a small card to be designed that will be included with our product when it ships. It will be 2 sided with 1 side being a "thank you" with our logo and the other side containing the following text:We would love to hear your feedback! For every review we receive on our products, we donate 100% of the proceeds of your order to TIDEWELL -- a non profit organization dedicated to preserving our oceans!If you are not 100% satisfied with your purchase or have any problems, we will always resolve your issue. please contact us via Brisko if you need assistance.Insert needs to be well organized and information presented in a clear and visually appealing way.
Target Market(s)
Women, aged 24-45
Colors
Designer to choose colors to be used in the design.
Look and feel
Each slider illustrates characteristics of the customer's brand and the style your logo design should communicate.

```html
<!DOCTYPE html>
<html lang="en">
<head>
<meta charset="utf-8">
<title>Summitvale Thank You Insert</title>
<link rel="stylesheet" href="https://fonts.googleapis.com/css2?family=Great+Vibes&family=Lato:wght@300;700&display=swap">
<style>
  :root {
    --page-bg: #ffffff;
    --frame: #7a7a7a;
    --sunrise: #f7a936;
    --lagoon: #1aa1b0;
    --ink-light: #ffffff;
  }
  html, body {
    margin: 0;
    padding: 0;
    width: 1200px;
    height: 1200px;
    overflow: hidden;
    background: var(--page-bg);
  }
  .sheet {
    position: relative;
    width: 1200px;
    height: 1200px;
    box-sizing: border-box;
    border: 1px solid var(--frame);
    font-family: "Lato", sans-serif;
  }
  .card {
    position: absolute;
    width: 793px;
    height: 526px;
    border-radius: 55px;
  }
  .card--front {
    left: 214px;
    top: 53px;
    background: var(--sunrise);
  }
  .card--back {
    left: 209px;
    top: 626px;
    background: var(--lagoon);
  }
  .brand {
    position: absolute;
    left: 0;
    right: 0;
    top: 140px;
    display: flex;
    align-items: center;
    justify-content: center;
    gap: 16px;
  }
  .brand__dot {
    width: 30px;
    height: 30px;
    border: 5px solid var(--ink-light);
    border-radius: 50%;
    box-sizing: border-box;
  }
  .brand__name {
    font-weight: 700;
    font-size: 46px;
    letter-spacing: 3px;
    color: var(--ink-light);
  }
  .thanks {
    position: absolute;
    left: 0;
    right: 0;
    top: 318px;
    margin: 0;
    font-family: "Great Vibes", cursive;
    font-weight: 400;
    font-size: 170px;
    line-height: 1;
    text-align: center;
    color: var(--ink-light);
  }
  .message {
    position: absolute;
    left: 46px;
    top: 62px;
    width: 701px;
    margin: 0;
    font-weight: 300;
    font-size: 32px;
    line-height: 38.5px;
    color: var(--ink-light);
    text-align: justify;
    text-align-last: center;
  }
</style>
</head>
<body>
  <main class="sheet">
    <section class="card card--front">
      <div class="brand">
        <span class="brand__dot"></span>
        <span class="brand__name">SUMMITVALE</span>
      </div>
      <p class="thanks">Thank you</p>
    </section>
    <section class="card card--back">
      <p class="message">We would love to hear your feedback! For every review we receive on our products, we donate 100% of the proceeds of your order to TIDEWELL -- a non profit organization dedicated to preserving our oceans!If you are not 100% satisfied with your purchase or have any problems, we will always resolve your issue. please contact us via Brisko if you need assistance.Insert needs to be well organized and information presented in a clear and visually appealing way.</p>
    </section>
  </main>
</body>
</html>
```